Amazing Homepage required for Ireland's Top Crowdfunding site

Design/ PSD Files required.

BrookLedger.com is the market leader in crowd lending/peer to peer lending in Ireland. Businesses/SME’s can borrow anything from €5,000 to €100,000 at interest rates much more favourable than those offered by the banks. BL is also a quicker and less bureaucratic than traditional lending institutions. We are a viable alternative to banks and traditional sources of finance.

Our lenders are members of the public and they can lend directly to Irish businesses in amounts from €50 to €2,000. They get a better rate of return than deposit accounts, as well as the feel good factor of supporting a local business.

We have just completed a full rebrand of our logo and colours and would now like to utilise these to best effect by implementing them in a total redesign of our homepage to attract borrowers and lenders. Please see the attached files for the brand guidelines and logo/colours to be used.

We are looking for a designer to utilise our new branding in a creative way, conveying that we are modern, trustworthy, competitive and friendly/local.

We currently have two different user groups:
1- Lenders; this currently consists of members of the public but in future will expand to include financial institutions

2- Business borrowers looking for funds for their business

Embracing and balancing both of these user groups is difficult so we would like the homepage to primarily target borrowers but incorporate clear alternative calls to action for lenders/prospective lenders as well.

We would like:
Infinite scroll homepage
New logo and tagline on a fixed header which should also include; ‘Marketplace’ ‘About’ ‘FAQ’ and a clear login button
A static full bleed image
Overlaid over this we would like a loan calculator in a similar style/functionality to this one on www.pelvaro.com. It should have:
an image of a slider icon with amounts from €0 to €100,000
A text field with ‘Business Loan amount’ which fills when the slider is moved
Then, a text field called ‘Monthly repayment’
An email field with a clear call to action ie ‘Go’ or ‘Get Started’
The purpose of this is to enable prospective borrowers to quickly and easily get a quote estimate for their loan
Underneath this we would like to have an alternate call to action to target prospective lenders; something like ‘Looking to Lend?’

Further down the page we would like to have a heading ‘What is Brook Ledger?’
(include information from company overview)

3 images to illustrate loans live in our Marketplace

Target Market(s)

This Homepge should appeal to small business owners

Industry/Entity Type

Crowd

Number of Pages Required

1 page

Font styles to use
Sans Serif

Requirements
Must have
• Linear clean and modern homepage
• Clear calls to action
Nice to have
• Ideas for how video/rich media might be incorporated into a future iteration of the homepage

```html
<!DOCTYPE html>
<html lang="en">
<head>
<meta charset="utf-8">
<title>Brook Ledger – Business Lending</title>
<link href="https://fonts.googleapis.com/css2?family=Lato:wght@300;400;700&family=Open+Sans:wght@400;600;700&display=swap" rel="stylesheet">
<style>
:root{
  --red:#e8392a;
  --gold:#b8972a;
  --ink:#222;
  --muted:#555;
  --band:#eef0f3;
  --calc-bg:#f4f4f4;
  --market-bg:#ececec;
  --blue:#2d8fd8;
  --track:#dde3e8;
  --dark:#1f1f1f;
  --footer:#141414;
  --bottom:#0b0b0b;
  --rule:#c9ccd0;
}
*{margin:0;padding:0;box-sizing:border-box}
html,body{width:1200px;height:2899px;overflow:hidden}
body{position:relative;font-family:"Lato",sans-serif;color:var(--ink);background:#fff}
.abs{position:absolute}
.center{left:0;width:1200px;text-align:center}
.accent{color:var(--red)}
/* header */
.site-header{position:absolute;left:0;top:0;width:1200px;height:130px;background:#fff}
.brand{position:absolute;left:92px;top:54px;display:flex;align-items:center;gap:10px}
.brand-mark{width:22px;height:22px;border-radius:50%;background:var(--red)}
.brand-name{font-size:21px;font-weight:700;color:#333;line-height:1}
.main-nav{position:absolute;top:54px;left:490px;font-size:17px}
.main-nav a{color:#222;text-decoration:none;position:absolute;white-space:nowrap}
.main-nav a.active{color:var(--red)}
.login-btn{position:absolute;left:1015px;top:48px;width:92px;height:37px;background:var(--red);color:#fff;font-weight:700;font-size:16px;display:flex;align-items:center;justify-content:center}
/* hero */
.hero{position:absolute;left:0;top:130px;width:1200px;height:444px;background:linear-gradient(100deg,#c9d2da 0%,#e9edf1 35%,#d7dee4 60%,#b7c2cc 100%)}
.hero-next{position:absolute;left:1104px;top:206px;width:32px;height:32px}
.loan-box{position:absolute;left:790px;top:328px;width:410px;height:98px;background:rgba(25,25,25,.85);border-left:3px solid var(--red);padding:22px 0 0 38px}
.loan-box h2{color:var(--red);font-weight:400;font-size:21px;letter-spacing:.3px}
.loan-box p{color:#ddd;font-size:12px;margin-top:8px}
/* lend band */
.intro{position:absolute;left:0;top:574px;width:1200px;height:486px;background:var(--band);border-bottom:1px solid var(--rule)}
.lend-text{left:163px;top:56px;font-size:19px}
.lend-btn{left:760px;top:46px;width:276px;height:44px;background:var(--gold);color:#222;font-weight:700;font-size:18px;letter-spacing:.5px;display:flex;align-items:center;justify-content:center}
.intro-rule{left:95px;top:136px;width:1010px;height:1px;background:#999}
.section-title{font-size:21px;font-weight:400;text-transform:uppercase}
.subtitle{font-size:11px;letter-spacing:.3px}
.dots{left:480px;top:258px;width:240px;height:1px;border-top:1px dotted #aaa}
.body-copy{font-size:12px;line-height:23px;color:var(--muted)}
.btn-red{background:var(--red);color:#fff;display:flex;align-items:center;justify-content:center}
/* calculator */
.calc{position:absolute;left:0;top:1060px;width:1200px;height:540px;background:var(--calc-bg);border-bottom:1px solid var(--rule)}
.calc-q{font-size:23px;color:#1d3347}
.calc-input{width:119px;height:34px;border:1px solid #8a9aa6;background:#fff;font-size:15px;padding:7px 12px;color:#333}
.step{width:28px;height:28px}
.track{height:10px;background:var(--track);border-radius:5px}
.fill{height:10px;background:var(--blue);border-radius:5px}
.handle{width:46px;height:46px;border-radius:50%;background:#fff;box-shadow:0 2px 6px rgba(0,0,0,.25)}
.sum-label{font-size:15px;color:#345}
.sum-value{font-size:22px;color:#1d3347}
.sum-op{font-size:38px;color:var(--blue);font-weight:700}
/* about */
.about{position:absolute;left:0;top:1600px;width:1200px;height:330px;background:#f7f7f7;border-bottom:1px solid var(--rule)}
/* market */
.market{position:absolute;left:0;top:1930px;width:1200px;height:512px;background:var(--market-bg)}
.caption{font-size:12px;text-align:center;color:#333}
.caption b{display:block;margin-top:10px;font-size:11px}
/* newsletter */
.newsletter{position:absolute;left:0;top:2442px;width:1200px;height:100px;background:var(--dark)}
.news-title{left:135px;top:38px;font-family:"Open Sans",sans-serif;font-weight:700;font-size:23px;color:#fff}
.news-input{left:384px;top:32px;width:371px;height:36px;background:#fff;font-family:"Open Sans",sans-serif;font-size:12px;color:#666;padding:11px 15px}
.news-btn{left:765px;top:32px;width:185px;height:38px;background:var(--gold);color:#fff;font-family:"Open Sans",sans-serif;font-weight:700;font-size:14px;display:flex;align-items:center;justify-content:center}
/* footer */
.site-footer{position:absolute;left:0;top:2542px;width:1200px;height:266px;background:var(--footer);font-family:"Open Sans",sans-serif}
.foot-head{font-size:14px;font-weight:700;color:#eee;letter-spacing:.3px}
.foot-list{list-style:none;font-size:11px;color:#888;line-height:26px}
.contact-line{display:flex;align-items:center;gap:10px}
.legal{position:absolute;left:0;top:2808px;width:1200px;height:91px;background:var(--bottom);font-family:"Open Sans",sans-serif;font-size:11px;color:#888;text-align:center;padding-top:36px}
</style>
</head>
<body>

<header class="site-header">
  <div class="brand"><span class="brand-mark"></span><span class="brand-name">Brook Ledger</span></div>
  <nav class="main-nav">
    <a class="active" style="left:0">Home</a>
    <a style="left:85px">About</a>
    <a style="left:172px">How it works</a>
    <a style="left:309px">Market place</a>
    <a style="left:443px">FAQ</a>
  </nav>
  <div class="login-btn">Login</div>
</header>

<section class="hero" role="img" aria-label="Office team of business people around a desk with a growth chart behind them">
  <svg class="hero-next" viewBox="0 0 32 32"><circle cx="16" cy="16" r="15" fill="rgba(0,0,0,.35)" stroke="#fff" stroke-width="1.5"/><path d="M13 9l7 7-7 7" fill="none" stroke="#fff" stroke-width="2"/></svg>
  <div class="loan-box">
    <h2>BUSINESS LOAN AMOUNT</h2>
    <p>Neque porro quisquam est, qui dolorem ipsum&nbsp; quia dolor</p>
  </div>
</section>

<section class="intro">
  <p class="abs lend-text">Sed ut perspiciatis unde omnis iste natus error sit voluptatem</p>
  <div class="abs lend-btn">LOOKING TO LEND?</div>
  <div class="abs intro-rule"></div>
  <h2 class="abs center section-title" style="top:192px">Welcome to our <span class="accent">Brook Ledger</span></h2>
  <p class="abs center subtitle" style="top:230px">SED UT PERSPICIATIS UNDE OMNIS ISTE NATUS ERROR SIT VOLUPTATEM ACCUSANTIUM</p>
  <div class="abs dots"></div>
  <p class="abs body-copy" style="left:150px;top:288px;width:900px;text-align:center;font-size:11.5px">Sed ut perspiciatis unde omnis iste natus error sit voluptatem accusantium doloremque laudantium, totam rem aperiam, eaque ipsa quae ab illo inventore veritatis et quasi architecto beatae vitae dicta sunt explicabo. Nemo enim ipsam voluptatem quia voluptas sit aspernatur aut odit aut fugit, sed quia consequuntur magni dolores eos qui ratione voluptatem sequi nesciunt</p>
  <div class="abs btn-red" style="left:523px;top:388px;width:154px;height:36px;font-size:14px">Read More</div>
</section>

<section class="calc">
  <h2 class="abs center section-title" style="top:50px">Finance loans <span class="accent">calculator</span></h2>
  <p class="abs body-copy" style="left:140px;top:100px;width:920px;text-align:center">Sed ut perspiciatis unde omnis iste natus error sit voluptatem accusantium doloremque laudantium, totam rem aperiam, eaque ipsa quae ab illo inventore veritatis et quasi architecto beatae vitae dicta sunt explicabo</p>

  <p class="abs calc-q" style="left:170px;top:208px">how much cash do you want?</p>
  <div class="abs calc-input" style="left:904px;top:196px">£&nbsp; 111</div>
  <svg class="abs step" style="left:171px;top:254px" viewBox="0 0 28 28"><circle cx="14" cy="14" r="13" fill="none" stroke="#555"/><path d="M9 14h10" stroke="#555" stroke-width="1.5"/></svg>
  <div class="abs track" style="left:230px;top:263px;width:733px"></div>
  <div class="abs fill" style="left:230px;top:263px;width:125px"></div>
  <svg class="abs handle" style="left:332px;top:245px" viewBox="0 0 46 46"><path d="M20 17l-5 6 5 6M26 17l5 6-5 6" fill="none" stroke="#333" stroke-width="2"/></svg>
  <svg class="abs step" style="left:993px;top:254px" viewBox="0 0 28 28"><circle cx="14" cy="14" r="13" fill="none" stroke="#555"/><path d="M9 14h10M14 9v10" stroke="#555" stroke-width="1.5"/></svg>

  <p class="abs calc-q" style="left:170px;top:312px">how long do you want it for?</p>
  <p class="abs" style="left:633px;top:322px;font-size:12px;color:#345">(Repayment date: Saturday 30th May 2015 )</p>
  <div class="abs calc-input" style="left:904px;top:302px">23<span style="margin-left:42px">days</span></div>
  <svg class="abs step" style="left:171px;top:358px" viewBox="0 0 28 28"><circle cx="14" cy="14" r="13" fill="none" stroke="#555"/><path d="M9 14h10" stroke="#555" stroke-width="1.5"/></svg>
  <div class="abs track" style="left:230px;top:367px;width:733px"></div>
  <div class="abs fill" style="left:230px;top:367px;width:555px"></div>
  <svg class="abs handle" style="left:762px;top:349px" viewBox="0 0 46 46"><path d="M20 17l-5 6 5 6M26 17l5 6-5 6" fill="none" stroke="#333" stroke-width="2"/></svg>
  <svg class="abs step" style="left:993px;top:358px" viewBox="0 0 28 28"><circle cx="14" cy="14" r="13" fill="none" stroke="#555"/><path d="M9 14h10M14 9v10" stroke="#555" stroke-width="1.5"/></svg>

  <div class="abs" style="left:170px;top:428px"><p class="sum-label">Borrowing</p><p class="sum-value">£111</p></div>
  <div class="abs sum-op" style="left:280px;top:420px">+</div>
  <div class="abs" style="left:343px;top:428px"><p class="sum-label">Interest</p><p class="sum-value">£20.42</p></div>
  <div class="abs sum-op" style="left:478px;top:420px">=</div>
  <div class="abs" style="left:543px;top:428px"><p class="sum-label">Total to repay</p><p class="sum-value">£131.42</p></div>
  <div class="abs btn-red" style="left:755px;top:426px;width:268px;height:60px;font-size:20px;font-weight:300">Apply now</div>
</section>

<section class="about">
  <h2 class="abs center section-title" style="top:56px">What is <span class="accent">Brook Ledger?</span></h2>
  <div class="abs" role="img" aria-label="Two colleagues reviewing paperwork at a laptop" style="left:100px;top:133px;width:175px;height:132px;background:linear-gradient(135deg,#dfe4ea,#9aa6b2)"></div>
  <p class="abs body-copy" style="left:328px;top:132px;width:772px;text-align:justify;font-size:11.5px;line-height:25px">Sed ut perspiciatis unde omnis iste natus error sit voluptatem accusantium doloremque laudantium, totam rem aperiam, eaque ipsa quae ab illo inventore veritatis et quasi architecto beatae vitae dicta sunt explicabo. Nemo enim ipsam voluptatem quia voluptas sit aspernatur aut odit aut fugit, sed quia consequuntur magni dolores eos qui ratione voluptatem sequi nesciunt Neque porro quisquam est, qui dolorem ipsum quia dolor sit amet, consectetur, adipisci velit, sed quia non numquam eius modi tempora incidunt ut labore et dolore magnam aliquam Neque porro quisquam est, qui dolorem ipsum quia dolor sit amet, consectetur, adipisci velit, sed quia non</p>
</section>

<section class="market">
  <h2 class="abs center section-title" style="top:64px">Finance loans in <span class="accent">our marketplace</span></h2>
  <p class="abs body-copy" style="left:140px;top:112px;width:920px;text-align:center">Sed ut perspiciatis unde omnis iste natus error sit voluptatem accusantium doloremque laudantium, totam rem aperiam, eaque ipsa quae ab illo inventore veritatis et quasi architecto beatae vitae dicta sunt explicabo</p>
  <div class="abs" role="img" aria-label="Hand signing a loan document with a gold pen" style="left:162px;top:202px;width:273px;height:196px;background:linear-gradient(135deg,#e9ddc8,#8c7a62)"></div>
  <div class="abs" role="img" aria-label="Businesswoman working with a calculator and keyboard at a desk" style="left:450px;top:202px;width:298px;height:196px;background:linear-gradient(135deg,#e7e6e4,#77706a)"></div>
  <div class="abs" role="img" aria-label="Business people reviewing charts on a tablet" style="left:765px;top:202px;width:273px;height:196px;background:linear-gradient(135deg,#dbe6f0,#4a6d93)"></div>
  <p class="abs caption" style="left:162px;top:420px;width:273px">Sed ut perspiciatis unde omnis<b>MAY 2015</b></p>
  <p class="abs caption" style="left:450px;top:420px;width:298px">Sed ut perspiciatis unde omnis<b>MAY 2015</b></p>
  <p class="abs caption" style="left:765px;top:420px;width:273px">Sed ut perspiciatis unde omnis<b>MAY 2015</b></p>
</section>

<section class="newsletter">
  <h2 class="abs news-title">NEWSLETTER SIGNUP</h2>
  <div class="abs news-input">ENTER YOUR EMAIL ID</div>
  <div class="abs news-btn">GET STARTED</div>
</section>

<footer class="site-footer">
  <h3 class="abs foot-head" style="left:196px;top:32px">WELCOME</h3>
  <ul class="abs foot-list" style="left:196px;top:64px">
    <li>Home</li><li>About</li><li>Market Place</li><li>FAQs</li><li>How it works</li><li>Lend</li><li>Borrow</li>
  </ul>
  <h3 class="abs foot-head" style="left:400px;top:32px">OUR MARKETPLACE</h3>
  <ul class="abs foot-list" style="left:400px;top:64px">
    <li>ed ut perspiciatis unde</li><li>omnis iste natus error</li><li>sit voluptatem accusantium</li><li>doloremque laudantium,</li><li>totam rem aperiam</li><li>eaque ipsa quae ab</li><li>illo inventore veritatis</li>
  </ul>
  <ul class="abs foot-list" style="left:622px;top:64px">
    <li>sit voluptatem accusantium</li><li>doloremque laudantium,</li><li>totam rem aperiam</li><li>eaque ipsa quae ab</li><li>illo inventore veritatis</li>
  </ul>
  <h3 class="abs foot-head" style="left:888px;top:32px">CONTACT INFO</h3>
  <ul class="abs foot-list" style="left:888px;top:64px">
    <li style="font-size:12px">Brook Ledger</li>
    <li>3 ed ut perspiciatis unde</li>
    <li>omnis iste natus</li>
    <li class="contact-line"><svg width="11" height="11" viewBox="0 0 24 24"><path fill="#888" d="M6.6 10.8a15 15 0 006.6 6.6l2.2-2.2c.3-.3.7-.4 1-.2 1.1.4 2.3.6 3.6.6.6 0 1 .4 1 1V20c0 .6-.4 1-1 1A17 17 0 013 4c0-.6.4-1 1-1h3.5c.6 0 1 .4 1 1 0 1.3.2 2.5.6 3.6.1.3 0 .7-.2 1z"/></svg>0145 332 610</li>
    <li class="contact-line"><svg width="11" height="11" viewBox="0 0 24 24"><path fill="#888" d="M6 3h12v5H6zM4 9h16a2 2 0 012 2v6h-4v4H6v-4H2v-6a2 2 0 012-2zm4 7v3h8v-3z"/></svg>0145 332 610</li>
  </ul>
</footer>

<div class="legal">Copyright © 2015 . Brookledger . All rights reserved.</div>

</body>
</html>
```